Wine Label for a White and a Red Wine from Italy

We have a very good idea of what we want with artwork. We need you to please design a 'template' with the text so we can change out the artwork from year to year. Samples are shown of what we are looking for. We are looking for options with the two basic designs. Brand name of wine is: Valora di Castegno. Both wines are in a light green Bordeaux-style bottle (note: we don't show a light green bottle in the mockup but please remember the bottle is light green). Artwork is provided. We'd like to see either the green or blue butterfly on the white wine, the red butterfly is for the red wine. Please base the design on the attached label from Brailey and/or the attached label from Chateau Mervanges.

Target Market(s)

Millennials, women

Requirements
Must have
• The artwork (butterflies) attached.
Nice to have
• Elegant, readable fonts. Please make the text so it can be changed by the printer. Please make it so the artwork can be changed too.

```html
<!DOCTYPE html>
<html lang="en">
<head>
<meta charset="utf-8">
<title>Valora di Castegno – Barrel Select Labels</title>
<link rel="stylesheet" href="https://fonts.googleapis.com/css2?family=Bodoni+Moda:ital,wght@0,400;1,400&family=Cormorant+Garamond:wght@400;500&family=Allura&display=swap">
<style>
  :root {
    --page: #ffffff;
    --frame: #b9b9b9;
    --ink: #1d1d1d;
    --ink-soft: #4a4a4a;
    --green-deep: #3f5a33;
    --green-wash: #a9c48c;
    --ochre: #f0a81c;
    --amber: #e6861a;
    --cream: #fbf3dc;
    --teal: #1b6f7a;
    --red: #c2331d;
  }
  * { box-sizing: border-box; margin: 0; padding: 0; }
  html, body { width: 738px; height: 1200px; overflow: hidden; background: var(--page); }
  .sheet { position: relative; width: 738px; height: 1200px; }

  .label {
    position: absolute;
    left: 24px;
    width: 690px;
    height: 346px;
    border: 1px solid var(--frame);
    background: var(--page);
    overflow: hidden;
  }
  .label--white-green { top: 38px; }
  .label--white-blue  { top: 424px; }
  .label--red         { top: 812px; }

  .artwork { position: absolute; inset: 0; }
  .label--white-green .artwork {
    background:
      radial-gradient(ellipse 110px 120px at 70px 150px, rgba(63,90,51,.85), rgba(169,196,140,.45) 60%, transparent 80%),
      radial-gradient(ellipse 120px 130px at 610px 170px, rgba(63,90,51,.85), rgba(169,196,140,.45) 60%, transparent 80%),
      radial-gradient(ellipse 160px 200px at 40px 220px, rgba(150,140,120,.25), transparent 75%),
      radial-gradient(ellipse 170px 200px at 650px 230px, rgba(150,140,120,.25), transparent 75%),
      var(--page);
  }
  .label--white-blue .artwork {
    background:
      radial-gradient(ellipse 90px 110px at 40px 200px, rgba(27,111,122,.9), transparent 80%),
      radial-gradient(ellipse 110px 120px at 570px 200px, rgba(27,111,122,.9), rgba(20,40,50,.4) 55%, transparent 80%),
      radial-gradient(ellipse 220px 260px at 60px 160px, var(--ochre), rgba(240,168,28,.6) 55%, transparent 85%),
      radial-gradient(ellipse 260px 300px at 640px 150px, var(--ochre), rgba(230,134,26,.7) 55%, transparent 85%),
      linear-gradient(90deg, var(--cream), var(--page) 40%, var(--page) 60%, var(--cream));
  }
  .label--red .artwork {
    background:
      radial-gradient(ellipse 110px 90px at 70px 190px, rgba(194,51,29,.95), transparent 80%),
      radial-gradient(ellipse 110px 120px at 540px 200px, rgba(194,51,29,.95), transparent 80%),
      radial-gradient(ellipse 230px 220px at 70px 90px, var(--ochre), rgba(240,168,28,.6) 55%, transparent 85%),
      radial-gradient(ellipse 260px 320px at 650px 140px, var(--ochre), rgba(230,134,26,.7) 55%, transparent 85%),
      linear-gradient(90deg, var(--cream), var(--page) 40%, var(--page) 60%, var(--cream));
  }

  .label-text {
    position: absolute;
    left: 50%;
    top: 0;
    transform: translateX(-50%);
    width: 300px;
    padding-top: 26px;
    text-align: center;
    color: var(--ink);
  }
  .brand-name {
    font-family: "Bodoni Moda", serif;
    font-weight: 400;
    font-size: 58px;
    line-height: 1;
  }
  .brand-sub {
    display: block;
    font-family: "Bodoni Moda", serif;
    font-size: 21px;
    line-height: 1.1;
    margin-top: 2px;
  }
  .cuvee {
    font-family: "Cormorant Garamond", serif;
    font-size: 15px;
    letter-spacing: 5px;
    color: var(--ink-soft);
    margin-top: 18px;
  }
  .details {
    font-family: "Cormorant Garamond", serif;
    font-size: 15px;
    line-height: 1.25;
    margin-top: 20px;
  }
  .divider {
    width: 12px;
    height: 1px;
    background: var(--ink);
    margin: 14px auto 12px;
  }
  .producer {
    font-family: "Cormorant Garamond", serif;
    font-size: 12.5px;
  }
  .farming {
    font-family: "Allura", cursive;
    font-size: 27px;
    margin-top: 8px;
  }
</style>
</head>
<body>
<main class="sheet">

  <section class="label label--white-green">
    <div class="artwork" role="img" aria-label="Artwork: two green butterflies in soft watercolour washes on white, one at each side"></div>
    <div class="label-text">
      <h1 class="brand-name">Valora<span class="brand-sub">di Castegno</span></h1>
      <p class="cuvee">BARREL SELECT</p>
      <p class="details">2018<br>Rosso<br>Piemonte, Italy</p>
      <div class="divider"></div>
      <p class="producer">Artisanally Crafted by Cantina Due Colli</p>
      <p class="farming">Sustainably Farmed</p>
    </div>
  </section>

  <section class="label label--white-blue">
    <div class="artwork" role="img" aria-label="Artwork: blue butterflies over golden yellow painted brushstrokes at both sides"></div>
    <div class="label-text">
      <h2 class="brand-name">Valora<span class="brand-sub">di Castegno</span></h2>
      <p class="cuvee">BARREL SELECT</p>
      <p class="details">2018<br>Rosso<br>Piemonte, Italy</p>
      <div class="divider"></div>
      <p class="producer">Artisanally Crafted by Cantina Due Colli</p>
      <p class="farming">Sustainably Farmed</p>
    </div>
  </section>

  <section class="label label--red">
    <div class="artwork" role="img" aria-label="Artwork: red butterflies over golden orange painted brushstrokes at both sides"></div>
    <div class="label-text">
      <h2 class="brand-name">Valora<span class="brand-sub">di Castegno</span></h2>
      <p class="cuvee">BARREL SELECT</p>
      <p class="details">2018<br>Rosso<br>Piemonte, Italy</p>
      <div class="divider"></div>
      <p class="producer">Artisanally Crafted by Cantina Due Colli</p>
      <p class="farming">Sustainably Farmed</p>
    </div>
  </section>

</main>
</body>
</html>
```